Wrelby needs a CD cover artwork for the song "Under Quiet Skies"

Hi, I need a CD cover artwork for my new song "Under Quiet Skies". I want to have an image of "Earth" for it. The earth image can be either picturesque or unique artistic. And also, it needs to contain the logo "Wrelby" and "Under Quiet Skies".
jpg. file is necessary.
And I don't like something purchased from the stock image which I need to pay additionally. Original image is preferable.

Target Market(s)

Music

Colors

Designer to choose colors to be used in the design.

Requirements
Must have
• -Earth image
• -The logo "Wrelby" and "Under Quiet Skies"
Nice to have
• -A whole globe image of the earth might be good, rather than a part of the globe or scene of the earth.
• -Something awe-inspiring image might be good.
• -The logo "Wrelby" and "Under Quiet Skies" better fuse to the image nicely rather than oddly standing out from the image.
Should not have
• -the stock image which I need to pay additionally

```html
<!DOCTYPE html>
<html lang="en">
<head>
<meta charset="utf-8">
<title>Wrelby – Under Quiet Skies</title>
<link rel="stylesheet" href="https://fonts.googleapis.com/css2?family=Antonio:wght@500;600&display=swap">
<style>
  :root {
    --sky-top: #f4f3f5;
    --sky-mid: #e2dde2;
    --sky-low: #b9aaae;
    --ink-navy: #101a26;
    --ink-brown: #3a2118;
    --globe-light: #f1eff2;
    --globe-mid: #8d8088;
    --globe-deep: #3c3440;
    --globe-night: #1a1f2c;
  }
  html, body {
    margin: 0;
    padding: 0;
    width: 1200px;
    height: 1200px;
    overflow: hidden;
  }
  .cover {
    position: relative;
    width: 1200px;
    height: 1200px;
    overflow: hidden;
    background: linear-gradient(180deg, var(--sky-top) 0%, var(--sky-mid) 45%, #cfc4c8 75%, var(--sky-low) 100%);
  }
  .cover-art {
    position: absolute;
    inset: 0;
    width: 1200px;
    height: 1200px;
  }
  .title-block {
    position: absolute;
    top: 104px;
    right: 98px;
    text-align: right;
    color: var(--ink-navy);
    font-family: "Antonio", "Arial Narrow", sans-serif;
  }
  .artist-name {
    margin: 0;
    font-size: 152px;
    font-weight: 600;
    line-height: 1;
    letter-spacing: 1px;
  }
  .song-title {
    margin: 8px 0 0;
    font-size: 40px;
    font-weight: 500;
    line-height: 1;
    letter-spacing: 0.5px;
  }
</style>
</head>
<body>
  <main class="cover">
    <svg class="cover-art" viewBox="0 0 1000 1000" xmlns="http://www.w3.org/2000/svg">
      <defs>
        <radialGradient id="globe-fill" cx="0.38" cy="0.35" r="0.75">
          <stop offset="0" stop-color="var(--globe-light)"/>
          <stop offset="0.35" stop-color="#c9c1c7"/>
          <stop offset="0.7" stop-color="var(--globe-mid)"/>
          <stop offset="1" stop-color="var(--globe-deep)"/>
        </radialGradient>
        <radialGradient id="globe-night-side" cx="0.8" cy="0.25" r="0.45">
          <stop offset="0" stop-color="var(--globe-night)" stop-opacity="0.85"/>
          <stop offset="1" stop-color="var(--globe-night)" stop-opacity="0"/>
        </radialGradient>
        <linearGradient id="line-ink" x1="0" y1="0" x2="0" y2="1">
          <stop offset="0" stop-color="var(--ink-navy)"/>
          <stop offset="1" stop-color="var(--ink-brown)"/>
        </linearGradient>
      </defs>

      <g class="globe" role="img" aria-label="Photograph of the whole Earth seen from space, in silvery monochrome with swirling white clouds over the Americas">
        <circle cx="505" cy="560" r="378" fill="url(#globe-fill)"/>
        <circle cx="505" cy="560" r="378" fill="url(#globe-night-side)"/>
      </g>

      <g class="guide-lines" fill="none" stroke="url(#line-ink)" stroke-linecap="butt">
        <line class="guide-line guide-line--long" x1="-10" y1="264" x2="1010" y2="932" stroke-width="12" gradientUnits="userSpaceOnUse"/>
        <line class="guide-line guide-line--bold" x1="405" y1="532" x2="38" y2="1010" stroke-width="22"/>
        <line class="guide-line guide-line--short" x1="-10" y1="848" x2="80" y2="908" stroke-width="12"/>
      </g>
    </svg>

    <header class="title-block">
      <h1 class="artist-name">Wrelby</h1>
      <p class="song-title">Under Quiet Skies</p>
    </header>
  </main>
</body>
</html>
```